Coffee - Forum Design

Guarantee Payment:
I will start this project without guaranteeing payment. Until I receive 3 interested Freelancers emailing me "ready to start work", then I will guarantee payment.

About my website:
It will be a forum based website catering towards coffee and the like.

Requirements:
This will be a fun and simple design task. It requires the freelancer to take the dimensions of the following website:
https://brightmarrowlabs.example/forums/
Please use the above website as your template.

And re-design it to suit my needs. Every single element in that the website above will be exactly the same. You can add personal touches to the design.

Theme:
Something fun and playful with a slight modern feel. Simple colours, nothing too crazy and bold. Preferably no dark colours.

Logo:
Is currently being finished off. Will be uploading in due course.

Thanks everyone and Good Luck,
Gareth
PS. Send me a message if you have any queries.

NOTE: The PSD file must be CSS friendly while slicing the template.

Target Market(s)

Coffee & Cafe lovers of all types

Industry/Entity Type

Catering

Requirements
Must have
• Dimensions for each elements of the website can be seen in the following website, please use this as a guide:

```html
<!DOCTYPE html>
<html lang="en">
<head>
<meta charset="utf-8">
<title>Roast Rambler – Coffee Forum</title>
<link rel="stylesheet" href="https://fonts.googleapis.com/css2?family=Figtree:ital,wght@0,400;0,500;0,600;0,700;1,400;1,700;1,800&display=swap">
<style>
:root{
  --bean-dark:#2a1a12;
  --bean-mid:#6b4a36;
  --band:#0f0b09;
  --footer:#140f0c;
  --footer-base:#0c0907;
  --paper:#efeeec;
  --ink:#1e1e1e;
  --nav:#4a4a4a;
  --brown:#5a4030;
  --bar:#b7b7b7;
  --panel:#dcdcdc;
  --panel-line:#c4c4c4;
  --panel-base:#c9c9c9;
  --white:#ffffff;
  --footer-head:#5e5248;
  --footer-link:#6f655c;
  --button:#6b4f3e;
  --field:#24201d;
}
*{box-sizing:border-box;margin:0;padding:0}
html,body{width:1111px;height:1200px;overflow:hidden}
body{position:relative;font-family:"Figtree",sans-serif;background:var(--paper);color:var(--ink)}
.abs{position:absolute}

.hero-photo{left:0;top:0;width:1111px;height:147px;background:radial-gradient(ellipse at 40% 30%,var(--bean-mid),var(--bean-dark) 70%)}
.account-band{left:0;top:147px;width:1111px;height:66px;background:var(--band)}
.account-link{top:30px;color:var(--white);font-size:14px;font-weight:600}
.field{top:17px;height:29px;width:148px;background:var(--field);color:#cfcfcf;font-size:11px;font-weight:600;padding:8px 10px}
.login-btn{left:1001px;top:16px;width:61px;height:31px;background:var(--button);border-radius:3px;color:var(--white);font-size:12px;font-weight:700;text-align:center;line-height:31px}

.brand{left:58px;top:232px;display:flex;align-items:center;gap:10px}
.brand-dot{width:36px;height:36px;border-radius:50%;background:var(--brown)}
.brand-name{font-size:22px;font-weight:700;color:var(--brown)}
.main-nav{top:240px;font-size:25px;font-weight:700;color:var(--nav);letter-spacing:.3px}

.results-bar{left:48px;top:296px;width:1015px;height:43px;background:var(--bar);border-radius:4px;color:var(--white);font-size:20px;padding:10px 20px;border-bottom:2px solid #9c9c9c}

.forum-title{left:53px;top:348px;font-size:54px;font-weight:800;font-style:italic;color:var(--brown)}
.topic-list{left:48px;top:413px;width:661px}
.topic{position:relative;height:110px;border-top:1px solid #bdbdbd;padding:12px 6px}
.topic-title{font-size:24px;font-weight:500}
.topic-author{font-size:19px;font-style:italic;color:#555;margin-top:2px}
.topic-meta{font-size:10px;color:#333;margin-top:4px}
.avatar{position:absolute;right:2px;top:10px;width:83px;height:76px;border:1px solid #bbb;background:#fff;padding:3px}
.avatar span{display:block;width:100%;height:100%;background:linear-gradient(135deg,#5a1a12,#2b1a14 60%,#a3241a)}

.pager{left:51px;top:952px;width:658px;height:46px;background:#d9d9d9;border:2px solid #c7c7c7;border-radius:8px;display:flex;justify-content:center;align-items:center;gap:9px}
.page{width:34px;height:34px;background:#f3f3f3;border:1px solid #c9c9c9;font-size:19px;font-weight:700;color:#444;text-align:center;line-height:32px}
.page.current{background:#b8b8b8}
.ellipsis{font-size:19px;color:#444}

.search{left:734px;top:351px;width:288px;height:54px;background:var(--white);border:1px solid #ddd;border-radius:8px;font-size:19px;color:#555;padding:14px 18px}
.search svg{position:absolute;right:14px;top:17px}

.filter-panel{left:734px;top:436px;width:288px;height:564px;background:var(--panel);border-radius:12px;overflow:hidden}
.panel-rule{position:absolute;left:0;width:288px;height:11px;background:var(--panel-line)}
.panel-base{position:absolute;left:0;bottom:0;width:288px;height:85px;background:var(--panel-base)}
.panel-heading{position:absolute;left:20px;font-size:23px;font-weight:700;color:var(--white)}
.option{position:absolute;left:20px;display:flex;align-items:center;font-size:12px;font-weight:700;color:#555}
.option i{width:20px;height:20px;border-radius:50%;background:#bdbdbd;border:1px solid #a9a9a9;margin-right:9px}
.option i.on{background:radial-gradient(circle,#3a2a22 45%,#8a7d75 50%)}
.option b{position:absolute;left:121px;font-weight:500;width:40px}
.panel-about{position:absolute;left:20px;top:367px;width:250px;font-size:15px;line-height:1.3;color:#555}
.panel-cta{position:absolute;left:20px;top:509px;font-size:15px;font-weight:700;color:#777}

.site-footer{left:0;top:1035px;width:1111px;height:120px;background:var(--footer)}
.footer-col{position:absolute;top:8px}
.footer-col h3{font-size:25px;font-weight:700;color:var(--footer-head)}
.footer-col a{display:block;font-size:18px;color:var(--footer-link);text-decoration:none;line-height:1.25}
.phone-dot{display:inline-block;width:12px;height:12px;border-radius:50%;background:#2f9fd8;margin:0 6px 0 -20px}
.copyright{left:0;top:1155px;width:1111px;height:45px;background:var(--footer-base);color:var(--white);font-size:17px;text-align:center;line-height:45px}
</style>
</head>
<body>

<div class="abs hero-photo" role="img" aria-label="Close-up photograph of roasted coffee beans"></div>

<div class="abs account-band">
  <span class="abs account-link" style="left:47px">Setup my account</span>
  <span class="abs account-link" style="left:201px">Forgot your password?</span>
  <span class="abs field" style="left:684px">Email or Phone number</span>
  <span class="abs field" style="left:843px">Password</span>
  <span class="abs login-btn">Login</span>
</div>

<div class="abs brand"><span class="brand-dot"></span><span class="brand-name">Roast Rambler</span></div>
<nav>
  <span class="abs main-nav" style="left:317px">PRODUCTS</span>
  <span class="abs main-nav" style="left:484px">SERVICES</span>
  <span class="abs main-nav" style="left:633px">FORUMS</span>
  <span class="abs main-nav" style="left:767px">HELP</span>
  <span class="abs main-nav" style="left:861px">BLOG</span>
  <span class="abs main-nav" style="left:955px">CONTACT</span>
</nav>

<div class="abs results-bar">There are 4000 total results, with 50 results per page.</div>

<h1 class="abs forum-title">Coffee Forum</h1>

<div class="abs topic-list">
  <div class="topic"><p class="topic-title">Premium organic coffee to be sold everywhere</p><p class="topic-author">by CoffeeMaster</p><p class="topic-meta">Posted 35 minutes ago (20 comments)</p><div class="avatar"><span role="img" aria-label="Member avatar"></span></div></div>
  <div class="topic"><p class="topic-title">Premium organic coffee to be sold everywhere</p><p class="topic-author">by CoffeeMaster</p><p class="topic-meta">Posted 35 minutes ago (20 comments)</p><div class="avatar"><span role="img" aria-label="Member avatar"></span></div></div>
  <div class="topic"><p class="topic-title">Premium organic coffee to be sold everywhere</p><p class="topic-author">by CoffeeMaster</p><p class="topic-meta">Posted 35 minutes ago (20 comments)</p><div class="avatar"><span role="img" aria-label="Member avatar"></span></div></div>
  <div class="topic"><p class="topic-title">Premium organic coffee to be sold everywhere</p><p class="topic-author">by CoffeeMaster</p><p class="topic-meta">Posted 35 minutes ago (20 comments)</p><div class="avatar"><span role="img" aria-label="Member avatar"></span></div></div>
  <div class="topic"><p class="topic-title">Premium organic coffee to be sold everywhere</p><p class="topic-author">by CoffeeMaster</p><p class="topic-meta">Posted 35 minutes ago (20 comments)</p><div class="avatar"><span role="img" aria-label="Member avatar"></span></div></div>
</div>

<div class="abs pager">
  <span class="page current">1</span><span class="page">2</span><span class="page">3</span><span class="page">4</span><span class="ellipsis">…</span><span class="page">11</span>
</div>

<div class="abs search">Search Topic ...
  <svg width="20" height="20" viewBox="0 0 20 20"><circle cx="8" cy="8" r="6" fill="none" stroke="#9a9a9a" stroke-width="2.5"/><line x1="12.5" y1="12.5" x2="18" y2="18" stroke="#9a9a9a" stroke-width="3" stroke-linecap="round"/></svg>
</div>

<aside class="abs filter-panel">
  <span class="panel-rule" style="top:191px"></span>
  <span class="panel-rule" style="top:348px"></span>
  <span class="panel-base"></span>
  <span class="panel-heading" style="top:52px">Product</span>
  <span class="option" style="top:89px"><i class="on"></i>Organic Coffee<b>(200)</b></span>
  <span class="option" style="top:113px"><i></i>Blended Coffee<b>(120)</b></span>
  <span class="option" style="top:138px"><i></i>Black Coffee<b>(110)</b></span>
  <span class="option" style="top:162px"><i></i>Latte<b>(170)</b></span>
  <span class="panel-heading" style="top:207px">Other Products</span>
  <span class="option" style="top:240px"><i class="on"></i>Hot Chocolate<b>(200)</b></span>
  <span class="option" style="top:264px"><i></i>Tea<b>(120)</b></span>
  <span class="option" style="top:289px"><i></i>Mocha<b>(150)</b></span>
  <span class="option" style="top:313px"><i></i>Milkshake<b>(179)</b></span>
  <p class="panel-about">This is a coffee community forum<br>where the coffee conneuseurs<br>talk about their day and how<br>the coffee has brighten up their<br>day. It's an important routine.</p>
  <p class="panel-cta">Come in and grab a coffee mate!</p>
</aside>

<footer class="abs site-footer">
  <div class="footer-col" style="left:84px"><h3>PRODUCTS</h3><a>Coffee</a><a>Beverages</a><a>Others</a></div>
  <div class="footer-col" style="left:270px"><h3>SERVICES</h3><a>Customers</a><a>Partners</a><a>Stocks</a></div>
  <div class="footer-col" style="left:456px"><h3>FORUMS</h3><a>Coffee talk</a><a>Geeking out</a></div>
  <div class="footer-col" style="left:623px"><h3>HELP</h3><a>Posts</a><a>Search</a><a>Products</a></div>
  <div class="footer-col" style="left:755px"><h3>BLOG</h3><a>Coffee Nerd</a><a>What kind?</a></div>
  <div class="footer-col" style="left:911px"><h3>CONTACT</h3><a>Site Map</a><a>Email</a><a><span class="phone-dot"></span>0800 555 014</a></div>
</footer>
<div class="abs copyright">© 2012 Roast Rambler</div>

</body>
</html>
```